Hair salon and Nail salon in Hawaii need a newspaper Ad design.

We need a newspaper Ad design for new open hair & nail salon in Waikiki Hawaii.Our Recommendation service for hair is "Head Spa" $30+tax and for nail is "Manicure Treatment Course" (Filing+Cuticle Care+Massage+Coloring) $20+tax.
We would like to see Hawaiian taste color and also having sense of luxury design. The ad size is W 5.0” x H 6.375”.
I would customers to know the shop place(Lanakila Crest Hotel 1F) , phone(808-555-0173), instagram(salonbrightwave) , our web site https://salonbrightwave.example and recommend services. For Web or Instagram , QR code is acceptable.

Target Market(s)

women & men

Industry/Entity Type

Beauty Salon

Font styles to use
Serif

Colors

Designer to choose colors to be used in the design.

Requirements
Must have
• Tagline for local customers. Shop Name is "SALON BRIGHTWAVE".the shop place(Lanakila Crest Hotel 1F) , phone(808-555-0173), instagram(salonbrightwave) and recommend services.
Nice to have
• Our services are competitive, but we don't want to be seen as just cheap and low quality.

```html
<!DOCTYPE html>
<html lang="en">
<head>
<meta charset="utf-8">
<title>Salon Brightwave – Newspaper Ad</title>
<link rel="stylesheet" href="https://fonts.googleapis.com/css2?family=Alfa+Slab+One&family=Playfair+Display:wght@500;700&family=Old+Standard+TT:wght@400;700&display=swap">
<style>
  :root {
    --ink: #0b0908;
    --wine: #4a0b07;
    --rust: #8e2206;
    --glow: #ffd84a;
    --gold: #f6b125;
    --cream: #fff7ea;
    --maroon-text: #6b0f0a;
    --hair-deep: #5c140c;
    --hair-mid: #9a3a1f;
    --hair-light: #c86a3e;
    --link: #7fe0f0;
  }
  * { box-sizing: border-box; margin: 0; padding: 0; }
  html, body { width: 1200px; height: 940px; overflow: hidden; background: #b9c4c6; }

  .ad {
    position: relative;
    width: 1200px; height: 940px;
    background: var(--ink);
    overflow: hidden;
    font-family: "Old Standard TT", Georgia, serif;
  }

  /* offer panel */
  .offer-panel {
    position: absolute; left: 380px; top: 190px; width: 820px; height: 560px;
    background:
      radial-gradient(ellipse 60% 70% at 70% 45%, #c2420a 0%, transparent 70%),
      linear-gradient(180deg, var(--rust) 0%, var(--wine) 100%);
  }

  .glow-band {
    position: absolute; left: 420px; width: 780px;
    background: linear-gradient(180deg, #b83a04 0%, #ff9d1f 30%, var(--glow) 50%, #ff9d1f 70%, #b83a04 100%);
    -webkit-mask-image: linear-gradient(90deg, transparent 0%, #000 30%, #000 100%);
            mask-image: linear-gradient(90deg, transparent 0%, #000 30%, #000 100%);
  }
  .glow-band--spa { top: 205px; height: 82px; }
  .glow-band--mani { top: 438px; height: 96px; }
  .glow-band--soft { top: 320px; height: 70px; opacity: .45; }

  .detail-strip, .location-strip {
    position: absolute; left: 420px; width: 780px;
    background: linear-gradient(90deg, transparent 0%, rgba(40,6,4,.85) 25%, rgba(40,6,4,.9) 100%);
  }
  .detail-strip { top: 536px; height: 42px; }
  .location-strip { top: 704px; height: 46px; background: linear-gradient(90deg, transparent 0%, #2a0806 25%, #2a0806 100%); }

  /* photo area */
  .portrait {
    position: absolute; left: 0; top: 0; width: 580px; height: 940px;
    background:
      radial-gradient(ellipse 40% 30% at 50% 28%, #e7b9a4 0%, transparent 70%),
      linear-gradient(100deg, var(--hair-deep) 0%, var(--hair-mid) 30%, var(--hair-light) 48%, var(--hair-mid) 65%, rgba(92,20,12,.6) 85%, rgba(74,11,7,0) 100%);
  }

  /* header */
  .masthead {
    position: absolute; left: 430px; top: 0; width: 770px; height: 190px;
    background: linear-gradient(90deg, rgba(11,9,8,0) 0%, var(--ink) 12%);
  }
  .brand-mark {
    position: absolute; left: 515px; top: 42px; width: 118px; height: 118px;
    background: linear-gradient(135deg, #3a3f3e, #6f7776);
    border: 3px solid #9aa3a2;
  }
  .brand-name {
    position: absolute; left: 660px; top: 40px; width: 520px;
    font-family: "Alfa Slab One", Georgia, serif;
    font-size: 58px; line-height: 62px; font-weight: 400;
    color: var(--gold); text-align: center;
    letter-spacing: 1px;
  }

  .service-title {
    position: absolute; left: 620px; width: 540px; text-align: center;
    font-family: "Alfa Slab One", Georgia, serif; font-weight: 400;
    color: var(--maroon-text);
  }
  .service-title--spa { top: 212px; font-size: 54px; line-height: 66px; }
  .service-title--mani { top: 446px; font-size: 36px; line-height: 42px; }

  .service-detail {
    position: absolute; left: 580px; top: 542px; width: 600px; text-align: center;
    font-size: 24px; line-height: 30px; color: var(--cream); letter-spacing: .3px;
  }

  .price-burst { position: absolute; width: 320px; height: 120px; left: 730px; }
  .price-burst--spa { top: 312px; }
  .price-burst--mani { top: 582px; }
  .price-burst svg { position: absolute; inset: 0; }
  .price-burst span {
    position: relative; display: block; text-align: center;
    font-family: "Alfa Slab One", Georgia, serif;
    font-size: 44px; line-height: 120px; color: var(--maroon-text);
  }

  .location {
    position: absolute; left: 620px; top: 708px; height: 38px;
    display: flex; align-items: center; gap: 12px;
    font-size: 30px; color: var(--cream);
  }

  .contact-bar {
    position: absolute; left: 430px; top: 750px; width: 770px; height: 190px;
    background: linear-gradient(90deg, rgba(11,9,8,0) 0%, var(--ink) 15%);
  }
  .phone {
    position: absolute; left: 560px; top: 752px; width: 640px; text-align: center;
    font-family: "Playfair Display", Georgia, serif; font-weight: 500;
    font-size: 86px; line-height: 110px; color: #ffffff; letter-spacing: 2px;
  }
  .online {
    position: absolute; left: 590px; top: 872px;
    display: flex; align-items: center; gap: 12px;
    font-size: 22px; color: var(--link);
  }
  .online .divider { width: 2px; height: 36px; background: #ffffff; margin: 0 6px; }
  .social-dot { width: 28px; height: 28px; border-radius: 8px; background: #d8357a; }
</style>
</head>
<body>
<main class="ad">
  <div class="offer-panel"></div>
  <div class="glow-band glow-band--spa"></div>
  <div class="glow-band glow-band--soft"></div>
  <div class="glow-band glow-band--mani"></div>
  <div class="detail-strip"></div>
  <div class="location-strip"></div>

  <div class="portrait" role="img" aria-label="Photo of a woman in profile with long glossy auburn hair"></div>

  <header class="masthead"></header>
  <div class="brand-mark"></div>
  <h1 class="brand-name">SALON<br>BRIGHTWAVE</h1>

  <h2 class="service-title service-title--spa">HEAD SPA</h2>
  <div class="price-burst price-burst--spa">
    <svg viewBox="-160 -60 320 120" aria-hidden="true"><polygon fill="#ffffff" points="150,0 125.6,8.2 138.6,21.1 106.4,23.4 106.1,38.9 71.2,34.9 57.5,50.8 25,41.2 0,55 -25,41.2 -57.5,50.8 -71.2,34.9 -106.1,38.9 -106.4,23.4 -138.6,21.1 -125.6,8.2 -150,0 -125.6,-8.2 -138.6,-21.1 -106.4,-23.4 -106.1,-38.9 -71.2,-34.9 -57.5,-50.8 -25,-41.2 0,-55 25,-41.2 57.5,-50.8 71.2,-34.9 106.1,-38.9 106.4,-23.4 138.6,-21.1 125.6,-8.2"/></svg>
    <span>$30+Tax.</span>
  </div>

  <h2 class="service-title service-title--mani">MANICURE TREATMENT<br>COURSE</h2>
  <p class="service-detail">(Filing+Cuticle Care+Massage+Coloring)</p>
  <div class="price-burst price-burst--mani">
    <svg viewBox="-160 -60 320 120" aria-hidden="true"><polygon fill="#ffffff" points="150,0 125.6,8.2 138.6,21.1 106.4,23.4 106.1,38.9 71.2,34.9 57.5,50.8 25,41.2 0,55 -25,41.2 -57.5,50.8 -71.2,34.9 -106.1,38.9 -106.4,23.4 -138.6,21.1 -125.6,8.2 -150,0 -125.6,-8.2 -138.6,-21.1 -106.4,-23.4 -106.1,-38.9 -71.2,-34.9 -57.5,-50.8 -25,-41.2 0,-55 25,-41.2 57.5,-50.8 71.2,-34.9 106.1,-38.9 106.4,-23.4 138.6,-21.1 125.6,-8.2"/></svg>
    <span>$20+Tax.</span>
  </div>

  <p class="location">
    <svg width="24" height="32" viewBox="0 0 24 32" aria-hidden="true"><path d="M12 1C6 1 1.5 5.5 1.5 11.5 1.5 19 12 31 12 31s10.5-12 10.5-19.5C22.5 5.5 18 1 12 1z" fill="none" stroke="#fff" stroke-width="3"/><circle cx="12" cy="11.5" r="4" fill="#fff"/></svg>
    Lanakila Crest Hotel 1F.
  </p>

  <footer class="contact-bar"></footer>
  <p class="phone">808-555-0173</p>
  <p class="online">
    <span class="social-dot"></span>
    <span>salonbrightwave</span>
    <span class="divider"></span>
    <svg width="28" height="28" viewBox="0 0 30 30" aria-hidden="true"><g fill="none" stroke="#fff" stroke-width="2"><circle cx="15" cy="15" r="13"/><ellipse cx="15" cy="15" rx="6" ry="13"/><line x1="2" y1="15" x2="28" y2="15"/><line x1="4" y1="8.5" x2="26" y2="8.5"/><line x1="4" y1="21.5" x2="26" y2="21.5"/></g></svg>
    <span>www.salonbrightwave.example</span>
  </p>
</main>
</body>
</html>
```